Pemo Menu 8.5"x14"

We are looking to touch up our design using the same elements and color scheme.

Target Market(s)

College students and middle income families

Industry/Entity Type

Restaurant

```html
<!DOCTYPE html>
<html lang="en">
<head>
<meta charset="utf-8">
<title>Pemo Street Food Menu</title>
<link href="https://fonts.googleapis.com/css2?family=Anton&family=Bebas+Neue&family=Courgette&family=Delius&family=Roboto:wght@400;700&display=swap" rel="stylesheet">
<style>
  :root{
    --page:#ffffff;
    --board-light:#383838;
    --board-dark:#1e1e1e;
    --chalk:#f2f2f2;
    --chalk-soft:rgba(255,255,255,.38);
    --red:#c62f28;
    --red-deep:#a3201b;
    --gold:#e8c53a;
    --gf:#8a5a2b;
    --vg:#2f8f3b;
    --veg:#9ccc1c;
    --local:#5cc546;
    --badge:#2a2a2a;
  }
  *{box-sizing:border-box;margin:0;padding:0}
  html,body{width:1200px;height:978px;overflow:hidden;background:var(--page)}
  body{position:relative;font-family:"Delius",sans-serif;color:var(--chalk)}

  .page-label{position:absolute;top:56px;font-family:"Roboto",sans-serif;font-size:14px;color:#111}
  .page-label.front{left:52px}
  .page-label.back{left:633px}

  .panel{position:absolute;top:83px;width:517px;height:850px;overflow:hidden;
    background:radial-gradient(ellipse at 45% 35%,var(--board-light),var(--board-dark) 80%)}
  .panel.front{left:52px}
  .panel.back{left:631px}

  /* brand */
  .brand{position:absolute;display:flex;align-items:center;justify-content:center}
  .brand-disc{position:absolute;border-radius:50%;background:var(--chalk)}
  .brand-name{position:relative;font-family:"Anton",sans-serif;color:var(--red);letter-spacing:2px}
  .front .brand{left:43px;top:14px;width:110px;height:110px}
  .front .brand-disc{width:106px;height:106px}
  .front .brand-name{font-size:32px}
  .back .brand{left:52px;top:0;width:150px;height:150px}
  .back .brand-disc{width:128px;height:128px}
  .back .brand-name{font-size:42px}

  /* section headings */
  .section-title{position:absolute;font-family:"Courgette",cursive;font-weight:400;font-size:19px;line-height:20px;color:var(--chalk);transform:rotate(-8deg);transform-origin:left bottom;white-space:nowrap}
  .swoosh{position:absolute;height:10px}
  .art{position:absolute;border-radius:8px;background:linear-gradient(160deg,#6a6a6a,#444)}

  /* menu boxes */
  .menu-box{position:absolute;width:215px;padding:7px 13px;border:1px dashed var(--chalk-soft)}
  .menu-box.wide{width:221px;padding:7px 11px 7px 17px}
  .item{margin-bottom:3.6px}
  .item:last-child{margin-bottom:0}
  .item-head{display:flex;justify-content:space-between;align-items:flex-start;font-size:8px;line-height:10.2px}
  .item-name{color:var(--red);text-transform:uppercase}
  .price{color:var(--gold);text-align:right;white-space:nowrap}
  .desc{font-size:8px;line-height:10.2px}
  .sub{padding-left:8px}
  .sub .item-name{text-transform:none}
  .dot{display:inline-block;width:6px;height:6px;border-radius:50%;vertical-align:-0.5px;margin-left:1px}
  .dot.gf{background:var(--gf)}
  .dot.vg{background:var(--vg)}
  .dot.v{background:var(--veg)}
  .dot.l{background:var(--local)}

  .intro{position:absolute;left:285px;top:76px;width:210px;font-size:7.6px;line-height:10px}

  /* legend */
  .legend{position:absolute;display:grid;grid-template-columns:74px auto;row-gap:9px;font-family:"Roboto",sans-serif;font-size:8px;white-space:nowrap}
  .legend span{display:flex;align-items:center;gap:5px}
  .legend b{display:inline-flex;align-items:center;justify-content:center;width:15px;height:15px;border-radius:50%;font-size:6px;color:#fff}
  .legend .gf b{background:var(--gf)}
  .legend .vg b{background:var(--vg)}
  .legend .v b{background:var(--veg)}
  .legend .l b{background:var(--local)}

  /* footer */
  .footer{position:absolute;width:225px}
  .store-row{display:flex;align-items:center;gap:6px}
  .store-badge{width:64px;height:19px;border-radius:4px;background:var(--badge);border:1px solid #777}
  .social{width:19px;height:19px;border-radius:50%;background:#cfcfcf}
  .store-row .social:first-of-type{margin-left:4px}
  .site{margin-top:9px;font-family:"Roboto",sans-serif;font-weight:700;font-size:18px;color:#fff;white-space:nowrap}

  /* promo */
  .promo-red{position:absolute;font-family:"Bebas Neue",sans-serif;color:var(--red-deep);font-size:100px;line-height:1;transform-origin:left top;white-space:nowrap}
  .promo-red.taco{left:253px;top:148px;transform:rotate(-9deg) scaleX(.85)}
  .promo-red.tuesday{left:267px;top:220px;transform:rotate(-8deg) scaleX(.8)}
  .promo-white{position:absolute;font-family:"Anton",sans-serif;color:#fff;line-height:1;transform-origin:left top;white-space:nowrap}
  .half{left:304px;top:356px;font-size:96px;transform:rotate(-4deg) scaleX(1.2)}
  .price-word{left:327px;top:486px;font-size:68px;transform:rotate(-5deg)}
  .tacos-word{left:339px;top:590px;font-size:62px;transform:rotate(-8deg)}
</style>
</head>
<body>
  <div class="page-label front">Front Page</div>
  <div class="page-label back">Back Page</div>

  <!-- FRONT -->
  <section class="panel front">
    <div class="brand"><span class="brand-disc"></span><span class="brand-name">PEMO</span></div>

    <h2 class="section-title" style="left:26px;top:150px">Chef’s Features</h2>
    <svg class="swoosh" style="left:28px;top:158px;width:128px" viewBox="0 0 150 10" preserveAspectRatio="none"><polygon points="0,9 150,0 150,2 2,10" fill="var(--gold)"/></svg>
    <div class="art" style="left:172px;top:120px;width:44px;height:42px" role="img" aria-label="Chalk drawing of a chef hat"></div>

    <div class="menu-box" style="left:14px;top:188px">
      <div class="item"><div class="item-head"><span class="item-name">Pho-rito</span><span class="price">$11.78</span></div>
        <p class="desc">Sliced steak / vietnamese noodles / bean sprouts / fresh basil &amp; cilantro / peanuts / infused thai chili oil</p></div>
      <div class="item"><div class="item-head"><span class="item-name">Pickle Brine Chicken Sandwich</span><span class="price">$12.48</span></div>
        <p class="desc">Local Harlow’s NON-GMO chicken thigh / pickle brine / green papaya slaw / grilled jalapeno / avocado ranch / Birch Oven brioche roll <span class="dot l"></span></p></div>
      <div class="item"><div class="item-head"><span class="item-name">Wisconsin Cheese Curds</span><span class="price">$8.78</span></div>
        <p class="desc">Cheddar curd / crispy batter / raspberry chili glaze</p></div>
      <div class="item"><div class="item-head"><span class="item-name">Arepas</span><span class="price">$5.88</span></div>
        <p class="desc">Corn flour dough griddled until crisp, split &amp; filled with traditional ingredients to make a sandwich. Choose from: <span class="dot l"></span></p></div>
      <div class="item sub"><div class="item-head"><span class="item-name">Carne Mechada (beef)</span></div>
        <p class="desc">Braised short rib / charred tomato butter / cotija cheese / pickled red onion</p></div>
      <div class="item sub"><div class="item-head"><span class="item-name">Rumbarria (pork)</span></div>
        <p class="desc">Local pulled pork / cotija / cilantro / diced onions / chipotle orange aioli</p></div>
      <div class="item"><div class="item-head"><span class="item-name">Pizza Frita</span><span class="price">$11.48</span></div>
        <p class="desc">Lightly fried crust / San Marzano tomatoes / roasted garlic / fresh basil / buffalo milk mozzarella</p></div>
      <div class="item"><div class="item-head"><span class="item-name">Chivito Steak Sandwich</span><span class="price">$10.99</span></div>
        <p class="desc">Sliced steak / Local ham / sunny side egg / provolone / char grilled red pepper/tomato golf salsa <span class="dot l"></span></p></div>
      <div class="item"><div class="item-head"><span class="item-name">Toritos</span><span class="price">$8.28</span></div>
        <p class="desc">Hot yellow peppers / queso blanco / crispy bacon corset <span class="dot gf"></span></p></div>
      <div class="item"><div class="item-head"><span class="item-name">Char Grilled Jerk Wings</span><span class="price">$10.49</span></div>
        <p class="desc">Jamaican jerk marinated chicken wings / Mezcal roasted mango puree / cilantro / lime wedge <span class="dot gf"></span></p></div>
    </div>

    <h2 class="section-title" style="left:26px;top:638px">Street Plates</h2>
    <svg class="swoosh" style="left:28px;top:652px;width:126px" viewBox="0 0 150 10" preserveAspectRatio="none"><polygon points="0,9 150,0 150,2 2,10" fill="var(--gold)"/></svg>
    <div class="art" style="left:140px;top:626px;width:40px;height:40px" role="img" aria-label="Chalk drawing of crossed fork and knife"></div>

    <div class="menu-box" style="left:14px;top:677px">
      <div class="item"><div class="item-head"><span class="item-name">Szechuan Pineapple Bowl</span><span class="price">$12.49</span></div>
        <p class="desc">Half fresh pineapple / jasmine rice / szechuan crispy chicken / thai chili peppers / sesame seeds / scallion</p></div>
      <div class="item"><div class="item-head"><span class="item-name">Fried Duck &amp; Waffle</span><span class="price">$14.99</span></div>
        <p class="desc">Roasted duck wings / tamarind glaze / sesame seeds / buttermilk waffle / maple ginger red cabbage</p></div>
      <div class="item"><div class="item-head"><span class="item-name">Bayou Street Plate</span><span class="price">$15.79</span></div>
        <p class="desc">Andouille sausage / fried catfish / Local Harlow’s NON-GMO chicken drumstick / molasses-cider slaw / collard greens / cornbread / honey compound butter</p></div>
    </div>

    <h2 class="section-title" style="left:294px;top:39px">Taco Truck</h2>
    <div class="art" style="left:400px;top:22px;width:56px;height:42px" role="img" aria-label="Chalk drawing of a taco"></div>

    <p class="intro">All tacos are served in pairs on lightly fried fresh corn tortillas with a side of house wonton chips or house corn chips (GF). Add a side of rice &amp; beans for $2.</p>

    <div class="menu-box wide" style="left:277px;top:118px">
      <div class="item"><div class="item-head"><span class="item-name">Korean Short Rib Tacos</span><span class="price">$8.49</span></div>
        <p class="desc">Braised beef / Koji slaw / charred tomato butter / soy chili glaze / grilled scallion</p></div>
      <div class="item"><div class="item-head"><span class="item-name">Carnitas Tacos</span><span class="price">$8.29</span></div>
        <p class="desc">Local pork carnitas / cilantro / chopped onion / chipotle orange aioli / shaved radish <span class="dot gf"></span> <span class="dot l"></span></p></div>
      <div class="item"><div class="item-head"><span class="item-name">Fried Green Tomato Tacos</span><span class="price">$8.29</span></div>
        <p class="desc">Cornmeal breaded tomatillo wedges / sweet corn relish / pickled jalapeno / poblano ranch <span class="dot gf"></span></p></div>
      <div class="item"><div class="item-head"><span class="item-name">Nigerian Suya Tacos</span><span class="price">$8.79</span></div>
        <p class="desc">Charred steak / organic peanut butter / suya spice / red onion / tomato / cilantro</p></div>
      <div class="item"><div class="item-head"><span class="item-name">Baja Fish Tacos</span><span class="price">$8.69</span></div>
        <p class="desc">Blackened mahi / charred pineapple salsa / slaw / avocado crema / tomatillo guacamole / avocado</p></div>
      <div class="item"><div class="item-head"><span class="item-name">Sweet Potato Kale Tacos</span><span class="price">$7.79</span></div>
        <p class="desc">Roasted sweet potato / sauteed kale / tomatilla guacamole / diced onion / avocado / kale chips / avocado crema <span class="dot gf"></span> <span class="dot v"></span></p></div>
      <div class="item"><div class="item-head"><span class="item-name">Mezcal Infused Chicken Tacos</span><span class="price">$8.49</span></div>
        <p class="desc">Harlow’s NON-GMO chicken thigh / Mezcal infusion / charred bell peppers &amp; spanish onion / smashed avocado / sour cream / lime wedge <span class="dot gf"></span> <span class="dot l"></span></p></div>
      <div class="item"><div class="item-head"><span class="item-name">New Orleans BBQ Shrimp Tacos</span><span class="price">$8.79</span></div>
        <p class="desc">Creole marinade / Tiger shrimp / green onion / lemon wedge / braised collard greens</p></div>
    </div>

    <h2 class="section-title" style="left:287px;top:458px">BAO Down</h2>
    <svg class="swoosh" style="left:285px;top:476px;width:98px" viewBox="0 0 150 10" preserveAspectRatio="none"><polygon points="0,9 150,0 150,2 2,10" fill="var(--gold)"/></svg>
    <div class="art" style="left:388px;top:444px;width:36px;height:29px" role="img" aria-label="Chalk drawing of a bao bun"></div>

    <div class="menu-box wide" style="left:277px;top:498px">
      <div class="item"><div class="item-head"><span class="item-name">Pork Belly Bao Bun</span><span class="price">$5.49</span></div>
        <p class="desc">Local pork belly / hoisin / sriracha mayo / pickled vegetables <span class="dot l"></span></p></div>
      <div class="item"><div class="item-head"><span class="item-name">Pineapple Teriyaki Bao Bun</span><span class="price">$5.29</span></div>
        <p class="desc">Crispy fried tofu / pineapple teriyaki sauce / sesame ginger broccoli slaw / pineapple salsa / grilled scallion <span class="dot vg"></span></p></div>
      <div class="item"><div class="item-head"><span class="item-name">Fried Chicken Bao Bun</span><span class="price">$5.49</span></div>
        <p class="desc">Local NON-GMO Harlow’s chicken / zesty orange sauce / sesame galbi cucumbers / toasted sesame seeds <span class="dot l"></span></p></div>
    </div>

    <div class="legend" style="left:279px;top:654px">
      <span class="gf"><b>GF</b>Gluten Free</span><span class="vg"><b>VG</b>Vegan</span>
      <span class="v"><b>V</b>Vegetarian</span><span class="l"><b>L</b>Locally Sourced</span>
    </div>

    <div class="footer" style="left:275px;top:786px">
      <div class="store-row">
        <span class="store-badge"></span><span class="store-badge"></span>
        <span class="social"></span><span class="social"></span><span class="social"></span>
      </div>
      <div class="site">www.pemostreetfood.com</div>
    </div>
  </section>

  <!-- BACK -->
  <section class="panel back">
    <div class="brand"><span class="brand-disc"></span><span class="brand-name">PEMO</span></div>

    <div class="art" style="left:392px;top:104px;width:106px;height:100px" role="img" aria-label="Chalk drawing of two tacos"></div>

    <div class="promo-red taco">TACO</div>
    <div class="promo-red tuesday">TUESDAY</div>
    <svg class="swoosh" style="left:314px;top:326px;width:152px;height:14px" viewBox="0 0 150 14" preserveAspectRatio="none"><polygon points="0,13 150,0 150,3 2,14" fill="var(--gold)"/></svg>
    <div class="promo-white half">1/2</div>
    <div class="promo-white price-word">PRICE</div>
    <div class="promo-white tacos-word">TACOS</div>

    <h2 class="section-title" style="left:25px;top:212px">Mac &amp; Cheese</h2>
    <svg class="swoosh" style="left:27px;top:220px;width:135px;height:14px" viewBox="0 0 150 14" preserveAspectRatio="none"><polygon points="0,13 150,0 150,2 2,14" fill="var(--gold)"/></svg>
    <div class="art" style="left:154px;top:174px;width:59px;height:55px" role="img" aria-label="Chalk drawing of a steaming bowl and spoon"></div>

    <div class="menu-box" style="left:14px;top:246px">
      <div class="item"><div class="item-head"><span class="item-name">Smoked Gouda Mac</span><span class="price">Half $6.49<br>Full $11.99</span></div>
        <p class="desc">Cavatappi pasta / béchamel / smoked gouda / toasted panko crumb <span class="dot v"></span></p></div>
      <div class="item"><div class="item-head"><span class="item-name">Bacon Smoked Gouda Mac</span><span class="price">Half $8.99<br>Full $15.49</span></div>
        <p class="desc">Cavatappi pasta / béchamel / smoked gouda / Local bacon / toasted panko bacon crumb <span class="dot l"></span></p></div>
      <div class="item"><div class="item-head"><span class="item-name">BBQ Shortrib Mac</span><span class="price">Half $8.99<br>Full $15.49</span></div>
        <p class="desc">Smoked gouda mac / bourbon bbq braised short rib / crispy fried shallots / smoked salt / panko bacon crumb</p></div>
      <div class="item"><div class="item-head"><span class="item-name">Crab Mac</span><span class="price">Half $8.99<br>Full $15.49</span></div>
        <p class="desc">Smoked gouda mac / deconstructed crab cake / parsley / lemon wedge</p></div>
      <div class="item"><div class="item-head"><span class="item-name">Southern Fried Mac &amp; Cheese</span><span class="price">Half $8.99<br>Full $15.49</span></div>
        <p class="desc">Smoked gouda mac / Local Harlow’s NON-GMO chicken drumstick / crumbled cornbread</p></div>
    </div>

    <h2 class="section-title" style="left:27px;top:528px">Burritos &amp;<br>Quesadillas</h2>
    <svg class="swoosh" style="left:31px;top:565px;width:98px" viewBox="0 0 150 10" preserveAspectRatio="none"><polygon points="0,9 150,0 150,2 2,10" fill="var(--gold)"/></svg>
    <div class="art" style="left:140px;top:506px;width:46px;height:58px" role="img" aria-label="Chalk drawing of a burrito"></div>

    <div class="menu-box" style="left:14px;top:590px">
      <div class="item"><div class="item-head"><span class="item-name">Huevos Rancheros Burrito</span><span class="price">$10.99</span></div>
        <p class="desc">Local eggs / black beans / charred street corn / spanish rice / crispy tortillas / pico de gallo / NY white cheddar / avocado crema <span class="dot v"></span> <span class="dot l"></span></p></div>
      <div class="item"><div class="item-head"><span class="item-name">Carnitas Chimichanga</span><span class="price">$10.29</span></div>
        <p class="desc">Local pork carnitas / NY white cheddar / black beans / rice / avocado crema / pico de gallo <span class="dot l"></span></p></div>
      <div class="item"><div class="item-head"><span class="item-name">Beef Bulgogi Burrito</span><span class="price">$11.79</span></div>
        <p class="desc">Marinated steak / purple cabbage / roasted asian pears / grilled scallion / jasmine rice / ginger wrap</p></div>
      <div class="item"><div class="item-head"><span class="item-name">Cornell Chicken Quesadilla</span><span class="price">$10.29</span></div>
        <p class="desc">NY white cheddar / cotija / scallion / avocado crema / smoked tomato salsa<br>Sub: Carnitas +1 / Short Rib +2</p></div>
    </div>

    <div class="legend" style="left:19px;top:798px">
      <span class="gf"><b>GF</b>Gluten Free</span><span class="vg"><b>VG</b>Vegan</span>
      <span class="v"><b>V</b>Vegetarian</span><span class="l"><b>L</b>Locally Sourced</span>
    </div>

    <div class="footer" style="left:272px;top:784px">
      <div class="store-row">
        <span class="store-badge"></span><span class="store-badge"></span>
        <span class="social"></span><span class="social"></span><span class="social"></span>
      </div>
      <div class="site" style="margin-top:7px">www.pemostreetfood.com</div>
    </div>
  </section>
</body>
</html>
```